Harbourlight Dental Centre Kelvale business cards and presentation folder

dental practice needing innovative black business cards for 2 different dentists witrh appointment details written at the back of the card for the patient.
name of dentists: Dr Anjali R Venkatesan B.D.S., M.P.H (Melb)
Dr. Raj Kalpat B.D.S.

Target Market(s)

professioinal, working class

Industry/Entity Type

Dental Clinic

Contact Information for Business Card

Dr. Raj Kalpat B.D.S.

Font styles to use
Sans Serif

Requirements
Must have
• Front side: logo
• dentist name
• phone number: 07- 5918 2243
• back side: appointment details: date, time,
• Address: 117C, 58 Tarrow Street, Kelvale - 4561, Queensland
• Email: admin@harbourlightdentalkelvale.example.au
• Website: www.harbourlightdental.example.au
• preferable logo colors
Nice to have
• classy look more pleasing

```html
<!DOCTYPE html>
<html lang="en">
<head>
<meta charset="utf-8">
<title>Harbourlight Dental Centre Kelvale – Business Card</title>
<link href="https://fonts.googleapis.com/css2?family=Roboto:wght@400;500&display=swap" rel="stylesheet">
<style>
  :root {
    --backdrop: #2b2624;
    --card-dark: #1d1c1d;
    --card-light: #c8d1d5;
    --accent-green: #a8c788;
    --text-light: #d9dcdc;
    --text-dark: #1e1f21;
    --divider: #8a8f7e;
  }
  * { margin: 0; padding: 0; box-sizing: border-box; }
  html, body { width: 1200px; height: 900px; overflow: hidden; }
  body {
    background: var(--backdrop);
    font-family: "Roboto", Arial, sans-serif;
    position: relative;
  }
  .card {
    position: absolute;
    width: 525px;
    height: 300px;
    border-radius: 3px;
    box-shadow: 0 12px 30px rgba(0,0,0,.45);
  }
  /* Front */
  .card-front {
    left: 50px; top: 300px;
    background: var(--card-dark);
    color: var(--text-light);
  }
  .front-brand {
    position: absolute;
    left: 40px; top: 128px;
    width: 220px;
    font-size: 21px;
    line-height: 1.2;
    font-weight: 400;
    color: var(--accent-green);
    letter-spacing: .5px;
    text-transform: uppercase;
  }
  .front-divider {
    position: absolute;
    left: 280px; top: 110px;
    width: 1px; height: 80px;
    background: var(--divider);
  }
  .dentist {
    position: absolute;
    left: 300px; top: 116px;
  }
  .dentist-name {
    font-size: 17px;
    font-weight: 500;
    color: var(--accent-green);
  }
  .dentist-credentials {
    margin-top: 4px;
    font-size: 13px;
    color: var(--accent-green);
  }
  .dentist-phone {
    margin-top: 6px;
    font-size: 17px;
    color: var(--text-light);
    display: flex; align-items: center; gap: 6px;
  }
  .dentist-phone svg { width: 13px; height: 13px; fill: var(--text-light); }

  /* Back */
  .card-back {
    left: 625px; top: 300px;
    background: var(--card-light);
    color: var(--text-dark);
  }
  .back-brand {
    position: absolute;
    right: 24px; top: 22px;
    width: 170px;
    text-align: right;
    font-size: 15px;
    line-height: 1.15;
    color: var(--text-dark);
    text-transform: uppercase;
  }
  .reminder-title {
    position: absolute;
    left: 30px; top: 72px;
    font-size: 14px;
    letter-spacing: .3px;
  }
  .reminder-form {
    position: absolute;
    left: 30px; top: 108px; right: 28px;
    font-size: 14px;
  }
  .form-row {
    display: flex; align-items: flex-end;
    height: 30px; gap: 6px;
  }
  .form-label { white-space: nowrap; }
  .form-line { flex: 1; border-bottom: 1px solid var(--text-dark); height: 18px; }
  .form-line.short { flex: 0 0 90px; }
  .form-line.medium { flex: 0 0 110px; }
  .contact {
    position: absolute;
    left: 30px; bottom: 20px;
    font-size: 11px;
    line-height: 1.65;
  }
</style>
</head>
<body>

  <section class="card card-front" aria-label="Business card front">
    <div class="front-brand">Harbourlight Dental Centre Kelvale</div>
    <div class="front-divider"></div>
    <div class="dentist">
      <p class="dentist-name">Dr Anjali R Venkatesan</p>
      <p class="dentist-credentials">B.D.S., M.P.H (Melb)</p>
      <p class="dentist-phone">
        <svg viewBox="0 0 24 24" aria-hidden="true"><path d="M6.6 10.8a15.1 15.1 0 0 0 6.6 6.6l2.2-2.2c.3-.3.7-.4 1-.2 1.1.4 2.3.6 3.6.6.6 0 1 .4 1 1V20c0 .6-.4 1-1 1A17 17 0 0 1 3 4c0-.6.4-1 1-1h3.5c.6 0 1 .4 1 1 0 1.3.2 2.5.6 3.6.1.3 0 .7-.2 1z"/></svg>
        07- 5918 2243
      </p>
    </div>
  </section>

  <section class="card card-back" aria-label="Business card back">
    <div class="back-brand">Harbourlight Dental Centre</div>
    <p class="reminder-title">APPOINTMENT REMINDER</p>
    <div class="reminder-form">
      <div class="form-row"><span class="form-label">FOR</span><span class="form-line"></span></div>
      <div class="form-row">
        <span class="form-label">DATE</span><span class="form-line short"></span>
        <span class="form-label">/</span><span class="form-line medium"></span>
        <span class="form-label">AT</span><span class="form-line"></span>
        <span class="form-label">AM/PM</span>
      </div>
      <div class="form-row"><span class="form-label">Note</span><span class="form-line"></span></div>
    </div>
    <div class="contact">
      <p>117C, 58 Tarrow Street, Kelvale - 4561, Queensland</p>
      <p>E: admin@harbourlightdentalkelvale.example.au</p>
      <p>W: www.harbourlightdental.example.au</p>
    </div>
  </section>

</body>
</html>
```